Certified Notary Signing Agent Business Card Design

I need a modern, visually appealing two-sided business card for my mobile notary signing agent business which clearly communicates my certification by the Federal Sealwork Guild ("FSG") and Deed Closing Method ("DCM"). It should be clean and easy to read and trust focused. While I am not committed to specific fonts and colors, I do like the colors in both my final logo and a sample logo (color examples only). I want to hand out a business card that is easy to locate in a stack and differentiates itself easily from others as it is an extremely crowded market space.

Target Market(s)

Title Companies, Escrow Officers, Real Estate Agents, Real Estate Lenders

Industry/Entity Type

Real Estate Lending

Contact Information for Business Card

I need a two-sided business card for my mobile notary signing agent business that prominently displays my photo, logo (potentially, just on the back), my service areas, phone, email, url and an FSG certification and DCM certification. On the back side of the card I would like my url, logo and potentially certification icons. On the back, I MAY want to add language that I have been an FSG Certified NSA for 10 + years and have performed over 8k in real estate loan transactions. I have attached a very old biz card circa 2007 that I designed myself on a card ordering platform. While it's not great, it can display how I crammed all of the data on a single card. I am NOT suggesting replicating this design in any form but provide it as reference material only,

Font styles to use
Sans Serif

Requirements
Must have
• Name: Marla Vostrick, Certified Notary Signing Agent Phone: 936.555.0142 URL: www.PrimeQuillSigners.com Email: marla@primequillsigners.com, Counties serviced: Montgomery, Grimes, N. Harris, Walker, Waller, Federal Sealwork Guild Badge, Deed Closing Method Badge (still need to upload this)
Nice to have
• I am open to color variations on my logo as illustrated in the attachment labeled as Logo Sample Colors Only (11A) that has a slate blue/grey background w/white lettering and gold pen and circles

```html
<!DOCTYPE html>
<html lang="en">
<head>
<meta charset="utf-8">
<title>Marla Vostrick – Business Card</title>
<link rel="stylesheet" href="https://fonts.googleapis.com/css2?family=Montserrat:wght@400;500;600&family=Playfair+Display:wght@400;500&display=swap">
<style>
  :root {
    --stage: #1b1b1e;
    --brown: #2f2219;
    --brown-deep: #261b14;
    --gold: #b8955a;
    --gold-light: #d4b47a;
    --gold-dark: #8c6c3c;
    --ink: #1f2a3d;
    --white: #f4efe7;
    --badge: #4a3827;
  }
  * { box-sizing: border-box; margin: 0; padding: 0; }
  html, body {
    width: 1200px; height: 948px; overflow: hidden;
    background: var(--stage);
  }
  .card {
    position: absolute; left: 220px; width: 760px; height: 434px;
    border-radius: 18px; overflow: hidden;
    background: linear-gradient(160deg, var(--brown) 0%, var(--brown-deep) 100%);
    color: var(--white);
    font-family: "Montserrat", sans-serif;
  }
  .card-back { top: 25px; }
  .card-front { top: 489px; }

  /* Back side */
  .brand {
    position: absolute; left: 0; top: 88px; width: 760px;
    text-align: center;
  }
  .brand-name {
    font-weight: 600; font-size: 24px; letter-spacing: 3px;
    line-height: 1.3; color: var(--white); text-transform: uppercase;
  }
  .stats {
    position: absolute; left: 0; top: 232px; width: 760px;
    display: flex; justify-content: center; align-items: center;
  }
  .stat {
    font-size: 14px; font-weight: 500; letter-spacing: 1px;
    line-height: 1.35; text-transform: uppercase; width: 260px;
  }
  .stat-left { text-align: right; }
  .stat .accent { color: var(--gold-light); }
  .stat-divider {
    width: 1px; height: 54px; margin: 0 22px;
    background: linear-gradient(var(--gold-dark), var(--gold-light), var(--gold-dark));
  }
  .url-band {
    position: absolute; left: 0; bottom: 0; width: 760px; height: 84px;
    background: linear-gradient(90deg, var(--gold-dark) 0%, var(--gold) 35%, var(--gold-light) 60%, var(--gold) 100%);
    border-top: 2px solid var(--gold-light);
    display: flex; align-items: center; justify-content: center;
  }
  .url-band span {
    font-family: "Playfair Display", serif; font-size: 25px;
    letter-spacing: 5px; color: var(--ink);
  }

  /* Front side */
  .portrait {
    position: absolute; left: 0; top: 0; width: 300px; height: 434px;
    background: linear-gradient(180deg, #a58452 0%, #8e6e40 55%, #2a211b 100%);
  }
  .identity { position: absolute; left: 340px; top: 72px; }
  .name {
    font-family: "Playfair Display", serif; font-weight: 400;
    font-size: 42px; letter-spacing: 1px; line-height: 1; text-transform: uppercase;
  }
  .title {
    margin-top: 10px; font-size: 14px; font-weight: 500; letter-spacing: 1.4px;
    color: var(--gold); text-transform: uppercase;
  }
  .contacts { position: absolute; left: 340px; top: 170px; list-style: none; }
  .contacts li {
    display: flex; align-items: center; gap: 10px;
    font-size: 16px; line-height: 30px;
  }
  .contacts svg { width: 18px; height: 18px; flex: none; }
  .rule {
    position: absolute; left: 340px; top: 282px; width: 270px; height: 1px;
    background: linear-gradient(90deg, var(--gold-light), transparent);
  }
  .service { position: absolute; left: 340px; top: 300px; }
  .service h2 {
    font-size: 17px; font-weight: 600; letter-spacing: 1px;
    color: var(--gold); text-transform: uppercase;
  }
  .service p { margin-top: 4px; font-size: 14px; line-height: 1.35; }
  .badges {
    position: absolute; right: 30px; bottom: 30px;
    display: flex; align-items: flex-end; gap: 22px;
  }
  .badge {
    display: block; border-radius: 50%;
    background: var(--badge);
  }
  .badge-method { width: 36px; height: 36px; }
  .badge-guild { width: 58px; height: 58px; }
</style>
</head>
<body>

<section class="card card-back">
  <div class="brand">
    <p class="brand-name">Prime Quill<br>Signing Agents</p>
  </div>
  <div class="stats">
    <p class="stat stat-left">FSG Certified NSA<br><span class="accent">for 10+ years</span></p>
    <span class="stat-divider"></span>
    <p class="stat stat-right"><span class="accent">Over 8,000</span> real estate<br>loan transactions</p>
  </div>
  <div class="url-band"><span>www.PrimeQuillSigners.com</span></div>
</section>

<section class="card card-front">
  <div class="portrait" role="img" aria-label="Portrait photo of Marla Vostrick in a black blazer on a gold background"></div>
  <div class="identity">
    <h1 class="name">Marla Vostrick</h1>
    <p class="title">Certified Notary Signing Agent</p>
  </div>
  <ul class="contacts">
    <li>
      <svg viewBox="0 0 18 18" aria-hidden="true"><circle cx="9" cy="9" r="8" fill="none" stroke="#b8955a" stroke-width="1.4"/><path d="M6 5.2l1.6-.4.9 2-1 .8a5 5 0 0 0 2.9 2.9l.8-1 2 .9-.4 1.6c-3.7.2-7-3.1-6.8-6.8z" fill="#b8955a"/></svg>
      936.555.0142
    </li>
    <li>
      <svg viewBox="0 0 18 18" aria-hidden="true"><circle cx="9" cy="9" r="8" fill="none" stroke="#b8955a" stroke-width="1.4"/><circle cx="9" cy="9" r="4.5" fill="none" stroke="#b8955a" stroke-width="1.1"/><path d="M4.5 9h9M9 4.5c-2 2.5-2 6.5 0 9M9 4.5c2 2.5 2 6.5 0 9" fill="none" stroke="#b8955a" stroke-width="1"/></svg>
      www.PrimeQuillSigners.com
    </li>
    <li>
      <svg viewBox="0 0 18 18" aria-hidden="true"><circle cx="9" cy="9" r="8" fill="none" stroke="#b8955a" stroke-width="1.4"/><rect x="4.8" y="6" width="8.4" height="6" fill="none" stroke="#b8955a" stroke-width="1.1"/><path d="M4.8 6L9 9.4 13.2 6" fill="none" stroke="#b8955a" stroke-width="1.1"/></svg>
      marla@primequillsigners.com
    </li>
  </ul>
  <div class="rule"></div>
  <div class="service">
    <h2>Proudly Serving</h2>
    <p>Montgomery, Grimes, N. Harris,<br>Walker and Waller</p>
  </div>
  <div class="badges">
    <span class="badge badge-method" role="img" aria-label="Deed Closing Method certification badge"></span>
    <span class="badge badge-guild" role="img" aria-label="Federal Sealwork Guild certification badge"></span>
  </div>
</section>

</body>
</html>
```